Engineering and Energy service provider

We need a design that gives the impression of a high level of technical competence and a reliable partner. Simple structure with little need for updates.
The company brand is Volnar and today consists of two main businesses: energy optimisation (Volnar energy) and technical consultancy (Volnar Engineering). Volnar energy is shown in the attached powerpoint,
We are a young growing company that consists of several businesses, the largest parts are energy monitoring services and consulting services. Consulting services for commercial installations in the technical area of cooling, ventilation, heating and energy. Services offered include project planning, project management, inspection, operational analysis and technical investigations. Energy monitoring and optimization services are performed as a subscription with a subscription to the service.
Target Market(s)
Commercial property owners Grocery retail, grocery stores, construction companies
Industry/Entity Type
energy services and consulting services
Coding
Coded - Design and coding required
Number of Pages Required
5+ page
Look and feel
Each slider illustrates characteristics of the customer's brand and the style your logo design should communicate.

```html
<!DOCTYPE html>
<html lang="en">
<head>
<meta charset="utf-8">
<title>Volnar — Smart Energy</title>
<link href="https://fonts.googleapis.com/css2?family=Orbitron:wght@700;800;900&family=Poppins:wght@400;500;600&display=swap" rel="stylesheet">
<style>
:root{
  --blue:#0a4cb0;
  --blue-dark:#083c8c;
  --blue-light:#3f86d6;
  --orange:#f26a1f;
  --amber:#fbb53a;
  --ink:#1c2430;
  --muted:#5a6270;
  --line:#d9dde3;
  --field:#f1f2f4;
  --white:#fff;
  --head:"Orbitron",sans-serif;
  --body:"Poppins",sans-serif;
}
*{box-sizing:border-box;margin:0;padding:0}
html,body{width:1200px;height:4854px;overflow:hidden}
body{font-family:var(--body);color:var(--ink);background:var(--white);position:relative}
.abs{position:absolute}
.h-title{font-family:var(--head);font-weight:900;text-transform:uppercase;letter-spacing:1px;line-height:1.05}
.btn{position:absolute;height:48px;display:flex;align-items:center;text-decoration:none;color:var(--white);font-family:var(--body);font-weight:600;font-size:12px;text-transform:uppercase;letter-spacing:.3px}
.btn .fill{position:absolute;inset:0;background:linear-gradient(90deg,var(--orange),#f59a2b 70%,var(--amber));clip-path:polygon(0 0,100% 0,82% 100%,0 100%)}
.btn .tail{position:absolute;right:8px;top:0;width:48px;height:48px;background:var(--white);clip-path:polygon(50% 0,100% 0,50% 100%,0 100%)}
.btn .lbl{position:relative;padding-left:34px}
.btn .chev{position:absolute;right:40px;top:14px;font-size:16px;color:var(--ink);font-weight:600}
.btn .chev.w{color:var(--white)}

/* header */
.site-header{position:absolute;left:0;top:0;width:1200px;height:88px;background:var(--white)}
.logo-text{font-family:var(--body);font-weight:600;text-transform:uppercase;letter-spacing:6px}
.site-header .logo-text{position:absolute;left:88px;top:22px;font-size:38px;color:var(--blue)}
.nav{position:absolute;left:418px;top:36px;display:flex;gap:28px;font-size:12.5px;text-transform:uppercase;color:var(--muted)}
.nav .active{color:var(--orange)}
.contact-btn{position:absolute;left:978px;top:24px;width:132px;height:42px;border:1.5px solid var(--ink);font-size:12px;font-weight:500;display:flex;align-items:center;justify-content:center;text-transform:uppercase}

/* hero */
.hero{position:absolute;left:0;top:88px;width:1200px;height:647px;background:var(--blue);overflow:visible}
.hero-photo{position:absolute;left:405px;top:34px;width:765px;height:672px;background:linear-gradient(135deg,#c9ced6,#e88a3a 55%,#4a5566);clip-path:polygon(33% 0,100% 0,67% 100%,0 100%);box-shadow:0 30px 40px rgba(0,0,0,.2)}
.hero-side{position:absolute;left:980px;top:166px;width:220px;height:362px;background:linear-gradient(160deg,var(--amber),var(--orange) 40%,#5a6f3a);clip-path:polygon(46% 0,100% 0,100% 100%,0 100%)}
.hero h1{position:absolute;left:88px;top:160px;font-size:62px;color:var(--white)}
.hero .sub{position:absolute;left:88px;top:278px;font-family:var(--head);font-weight:800;font-size:32px;color:var(--white);letter-spacing:1px}
.hero p{position:absolute;left:88px;top:332px;width:420px;font-size:14px;line-height:21px;color:var(--white)}
.mouse{position:absolute;left:90px;top:570px;width:18px;height:28px;border:2px solid var(--white);border-radius:9px}
.mouse::after{content:"";position:absolute;left:6px;top:5px;width:2px;height:6px;background:var(--white);border-radius:1px}
.slide-arrow{position:absolute;top:562px;width:50px;height:50px}

/* intro */
.section-title{position:absolute;left:0;width:1200px;text-align:center;color:var(--ink);font-size:31px}
.section-sub{position:absolute;left:0;width:1200px;text-align:center;font-size:14.5px;color:var(--ink)}
.photo-frame-bg{position:absolute;background:#dfe5ee;clip-path:polygon(15% 0,100% 0,85% 100%,0 100%)}
.photo{position:absolute;box-shadow:0 24px 30px rgba(0,0,0,.18)}
.intro-copy{position:absolute;left:697px;top:1156px;width:400px}
.intro-copy h3{font-family:var(--head);font-weight:700;font-size:16px;text-transform:uppercase;letter-spacing:.5px;margin-bottom:18px}
.intro-copy p{font-size:14.5px;line-height:24px;color:var(--muted)}

/* services */
.services{position:absolute;left:88px;top:1707px;width:1024px;height:262px;display:grid;grid-template-columns:repeat(4,1fr);border:1.5px solid var(--line)}
.service{position:relative;border-right:1.5px solid var(--line);padding:30px 26px 0 28px;overflow:hidden}
.service:last-child{border-right:0}
.service h4{font-family:var(--head);font-weight:800;font-size:14px;line-height:17px;text-transform:uppercase;margin-bottom:12px}
.service p{font-size:12.5px;line-height:19px;color:var(--muted)}
.service .tile{position:absolute;left:0;bottom:0;width:180px;height:100px;background:var(--blue);clip-path:polygon(52% 0,100% 0,48% 100%,0 100%)}
.service svg{position:absolute;left:60px;bottom:20px}

/* optimisation band */
.band{position:absolute;left:0;top:2178px;width:1200px;height:539px;background:var(--blue);overflow:hidden}
.band .light{position:absolute;left:640px;top:0;width:560px;height:539px;background:var(--blue-light);clip-path:polygon(42% 0,100% 0,100% 100%,0 100%)}
.band h2{position:absolute;left:88px;top:124px;font-size:31px;color:var(--white)}
.band p{position:absolute;left:88px;top:240px;width:490px;font-size:14.5px;line-height:24px;color:var(--white)}
.laptop-screen{position:absolute;left:645px;top:112px;width:450px;height:290px;border-radius:12px 12px 0 0;background:#1b1f26;padding:10px}
.laptop-screen div{width:100%;height:100%;background:linear-gradient(135deg,#8aa2b8,#e9edf2 55%,#f6f7f9)}
.laptop-base{position:absolute;left:593px;top:402px;width:551px;height:12px;border-radius:0 0 14px 14px;background:linear-gradient(#e9ebee,#9aa0a8)}

/* sectors */
.sectors{position:absolute;left:88px;top:2956px;display:flex;gap:15px}
.sector{width:244px;height:328px;border:1.5px solid var(--line);background:var(--white)}
.sector .ph{height:253px}
.sector h4{font-family:var(--head);font-weight:800;font-size:13.5px;line-height:17px;text-transform:uppercase;padding:12px 0 0 28px}

/* form */
.contact-form{position:absolute;left:712px;top:3622px;width:352px}
.contact-form label{display:block;font-size:10px;font-weight:600;text-transform:uppercase;margin-bottom:5px}
.contact-form .field{height:42px;background:var(--field);font-size:11.5px;color:#8a9098;padding:12px 24px;margin-bottom:14px}
.contact-form .field.area{height:93px}

/* cta band */
.cta{position:absolute;left:0;top:4183px;width:1200px;height:192px;background:linear-gradient(90deg,var(--orange),#f5932b 45%,var(--amber))}
.cta .badge{position:absolute;left:88px;top:25px;width:142px;height:142px;border-radius:50%;background:var(--white)}
.cta h2{position:absolute;left:266px;top:68px;font-size:32px;color:var(--white)}
.cta p{position:absolute;left:266px;top:112px;font-size:14px;color:var(--white)}
.cta .go{position:absolute;left:1036px;top:60px;width:72px;height:72px;border-radius:50%;background:var(--white)}

/* footer */
.site-footer{position:absolute;left:0;top:4375px;width:1200px;height:479px;background:var(--blue);color:var(--white)}
.site-footer .logo-text{position:absolute;left:88px;top:150px;font-size:44px;color:var(--white)}
.social{position:absolute;top:223px;width:48px;height:48px;border-radius:50%;background:#2a64be}
.fcol{position:absolute;top:122px}
.fcol h5{font-family:var(--head);font-weight:800;font-size:15px;text-transform:uppercase;letter-spacing:.5px;margin-bottom:26px}
.fcol li{list-style:none;font-size:12.5px;line-height:31px}
.fcol p{font-size:12.5px;line-height:21px;width:320px}
.news{position:absolute;left:582px;top:220px;width:326px;height:43px;background:var(--white);border:2px solid var(--white)}
.news span{position:absolute;left:14px;top:11px;font-size:12px;color:#8a9098}
.news b{position:absolute;right:2px;top:2px;width:102px;height:35px;background:var(--blue);font-size:11px;display:flex;align-items:center;justify-content:center;text-transform:uppercase}
.site-footer hr{position:absolute;left:88px;top:411px;width:1024px;border:0;border-top:1px solid rgba(255,255,255,.3)}
.copy{position:absolute;left:0;top:433px;width:1200px;text-align:center;font-family:var(--head);font-weight:700;font-size:12px;letter-spacing:.5px;text-transform:uppercase}
.chat{position:absolute;left:1127px;top:386px;width:54px;height:54px;border-radius:50%;background:var(--orange)}
</style>
</head>
<body>

<header class="site-header">
  <div class="logo-text">Volnar</div>
  <nav class="nav">
    <span class="active">Home</span><span>About Us</span><span>Services</span><span>Industries</span><span>Latest News</span><span>Careers</span>
  </nav>
  <div class="contact-btn">Contact Us</div>
</header>

<section class="hero">
  <div class="hero-photo" role="img" aria-label="Engineer in hard hat and high-visibility jacket working on rooftop cooling units"></div>
  <div class="hero-side" role="img" aria-label="Technician in orange safety gear on a roof ladder"></div>
  <h1 class="h-title">Smart<br>Energy.</h1>
  <div class="sub">RELIABLE RESULTS.</div>
  <p>Empowering commercial buildings with intelligent monitoring, optimization, and consulting solutions.</p>
  <a class="btn" style="left:88px;top:400px;width:244px"><span class="fill"></span><span class="tail"></span><span class="lbl">Get a Consultation</span><span class="chev">»</span></a>
  <div class="mouse"></div>
  <svg class="slide-arrow" style="left:1019px" viewBox="0 0 50 50"><circle cx="25" cy="25" r="23" fill="none" stroke="#fff" stroke-width="1.5"/><path d="M31 25H19M24 20l-5 5 5 5" fill="none" stroke="#fff" stroke-width="1.5"/></svg>
  <svg class="slide-arrow" style="left:1075px" viewBox="0 0 50 50"><circle cx="25" cy="25" r="23" fill="none" stroke="#fff" stroke-width="1.5"/><path d="M19 25h12M26 20l5 5-5 5" fill="none" stroke="#fff" stroke-width="1.5"/></svg>
</section>

<h2 class="section-title h-title" style="top:910px">Your Partner in Energy<br>Efficiency and Technical<br>Excellence</h2>
<div class="photo-frame-bg" style="left:155px;top:1055px;width:420px;height:475px"></div>
<div class="photo" style="left:120px;top:1102px;width:511px;height:375px;background:linear-gradient(135deg,#cfd3d8,#6f7a86 50%,#2a3440)" role="img" aria-label="Two engineers in hard hats reviewing energy data on monitors"></div>
<div class="intro-copy">
  <h3>Volnar Energy</h3>
  <p>We are a young and growing company with a strong technical background in energy monitoring and consulting. Our team specializes in cooling, ventilation, heating, and energy systems — delivering data-driven insights and reliable solutions for commercial installations.</p>
</div>
<a class="btn" style="left:697px;top:1364px;width:244px"><span class="fill"></span><span class="tail"></span><span class="lbl">Explore Our Services</span><span class="chev">»</span></a>

<h2 class="section-title h-title" style="top:1608px">Our Services</h2>
<div class="section-sub" style="top:1652px">Comprehensive support for every stage of your technical and energy projects.</div>
<div class="services">
  <div class="service"><h4>Energy Monitoring &amp; Optimization</h4><p>Monitor, analyze, and improve your energy performance...</p><span class="tile"></span>
    <svg width="50" height="50" viewBox="0 0 50 50" fill="none" stroke="#fff" stroke-width="2"><circle cx="25" cy="27" r="17"/><path d="M25 27l8-8M17 34h16"/></svg></div>
  <div class="service"><h4>Project Planning &amp; Management</h4><p>From design to completion, our experts ensure every project...</p><span class="tile"></span>
    <svg width="50" height="50" viewBox="0 0 50 50" fill="none" stroke="#fff" stroke-width="2"><rect x="9" y="6" width="26" height="36"/><path d="M14 14h16M14 22h16M14 30h8"/><circle cx="36" cy="36" r="9"/><path d="M36 31v5h4"/></svg></div>
  <div class="service"><h4>Technical Consulting</h4><p>In-depth consulting for cooling, ventilation, heating, and...</p><span class="tile"></span>
    <svg width="50" height="50" viewBox="0 0 50 50" fill="none" stroke="#fff" stroke-width="2"><circle cx="17" cy="24" r="6"/><path d="M6 44c0-8 5-12 11-12s11 4 11 12"/><rect x="24" y="6" width="20" height="20"/><path d="M28 12h12M28 18h8"/></svg></div>
  <div class="service"><h4>Operational Analysis...</h4><p>Detailed inspections and performance analyses...</p><span class="tile"></span>
    <svg width="50" height="50" viewBox="0 0 50 50" fill="none" stroke="#fff" stroke-width="2"><circle cx="25" cy="16" r="10"/><circle cx="25" cy="16" r="4"/><circle cx="13" cy="38" r="5"/><circle cx="37" cy="38" r="5"/><path d="M25 26v8M16 34l6-5M34 34l-6-5"/></svg></div>
</div>
<a class="btn" style="left:477px;top:2031px;width:246px"><span class="fill"></span><span class="tail"></span><span class="lbl" style="padding-left:40px">View All Services</span><span class="chev">»</span></a>

<section class="band">
  <div class="light"></div>
  <h2 class="h-title">Continuous<br>Energy Optimization<br>Simplified</h2>
  <p>Our subscription-based energy monitoring platform provides real-time insights, regular reports, and optimization recommendations — helping you reduce costs and environmental impact without extra effort.</p>
  <a class="btn" style="left:88px;top:373px;width:244px"><span class="fill"></span><span class="tail"></span><span class="lbl" style="padding-left:48px">Subscribe Now</span><span class="chev">»</span></a>
  <div class="laptop-screen"><div role="img" aria-label="Energy monitoring dashboard with wind power charts and readings"></div></div>
  <div class="laptop-base"></div>
</section>

<h2 class="section-title h-title" style="top:2826px">Trusted by Leading<br>Commercial Sectors</h2>
<div class="section-sub" style="top:2904px">We deliver energy-efficient and technically sound solutions across industries.</div>
<div class="sectors">
  <div class="sector"><div class="ph" style="background:linear-gradient(135deg,#e8c9a8,#8a6a50 60%,#3d4a5a)" role="img" aria-label="Property owners reviewing documents"></div><h4>Commercial<br>Property Owners</h4></div>
  <div class="sector"><div class="ph" style="background:linear-gradient(160deg,#dfe3e6,#9a8a6a 50%,#4c5560)" role="img" aria-label="Supermarket aisle with stocked shelves"></div><h4>Grocery Retail<br>&amp; Supermarkets</h4></div>
  <div class="sector"><div class="ph" style="background:linear-gradient(150deg,#a9c2d8,#7a8a92 50%,#e08a3a)" role="img" aria-label="Construction worker on site with scaffolding"></div><h4>Construction<br>Companies</h4></div>
  <div class="sector"><div class="ph" style="background:linear-gradient(135deg,#8aa6c4,#d9a36a 55%,#3a4656)" role="img" aria-label="Facility managers in hard hats in an industrial hall"></div><h4>Facility<br>Management Firms</h4></div>
</div>
<a class="btn" style="left:477px;top:3325px;width:246px"><span class="fill"></span><span class="tail"></span><span class="lbl" style="padding-left:42px">Request a Quote</span><span class="chev">»</span></a>

<h2 class="section-title h-title" style="top:3476px">Let’s Make Your Energy<br>Systems Smarter</h2>
<div class="photo-frame-bg" style="left:155px;top:3580px;width:420px;height:480px"></div>
<div class="photo" style="left:120px;top:3630px;width:511px;height:373px;background:linear-gradient(135deg,#c9b26a,#2d4f8a 45%,#d8772f)" role="img" aria-label="Team of engineers in hard hats and safety vests"></div>
<div class="contact-form">
  <label>Name*</label><div class="field">Enter your name</div>
  <label>Company*</label><div class="field">Enter company name</div>
  <label>Email*</label><div class="field">Enter email</div>
  <label>Message*</label><div class="field area"></div>
</div>
<a class="btn" style="left:712px;top:3960px;width:244px"><span class="fill"></span><span class="tail"></span><span class="lbl" style="padding-left:42px">Request a Quote</span><span class="chev">»</span></a>

<section class="cta">
  <div class="badge"></div>
  <h2 class="h-title">Korvain Energy Solutions</h2>
  <p>Reliable partner for energy monitoring and technical consulting.</p>
  <svg class="go" viewBox="0 0 72 72"><circle cx="36" cy="36" r="36" fill="#fff"/><path d="M26 36h20M40 30l6 6-6 6" fill="none" stroke="#1c2430" stroke-width="2"/></svg>
</section>

<footer class="site-footer">
  <div class="logo-text">Volnar</div>
  <span class="social" style="left:125px"></span>
  <span class="social" style="left:187px"></span>
  <span class="social" style="left:249px"></span>
  <div class="fcol" style="left:405px"><h5>Quick Link</h5><ul><li>About Us</li><li>Our Services</li><li>Projects</li><li>Blog</li><li>Contact Us</li></ul></div>
  <div class="fcol" style="left:582px"><h5>Subscribe Newsletter</h5><p>Get our monthly newsletter and marketing tips, straight to your inbox</p></div>
  <div class="news"><span>Enter your email</span><b>Subscribe</b></div>
  <div class="fcol" style="left:968px"><h5>Information</h5><ul><li>Have feedback?</li><li>Let us know!</li><li>Privacy Policy</li><li>Terms of Use</li><li>Locations</li></ul></div>
  <hr>
  <div class="copy">© 2025 Global Volnar. All rights reserved.</div>
  <svg class="chat" viewBox="0 0 54 54"><circle cx="27" cy="27" r="27" fill="#f26a1f"/><path d="M16 20h22v13H25l-6 5v-5h-3z" fill="none" stroke="#fff" stroke-width="2"/></svg>
</footer>

</body>
</html>
```